Hot-air ballooning company needs a DL-size flyer

Skylark Aerial Tours is a hot-air ballooning company which flies passengers in the King Valley, Victoria, Australia.
We need a 2-sided DL-size flyer which promotes our hot-air balloon flights and packages.
Most of our customers are couples, and we want the flyer design to communicate safety, adventure, and romance.
The flyer should make the best use of our images which we provide, and we've also included a document with the text for the flyer.
Updates

2 days is not long enough to gather designs, the brief never asked me what my deadline should be.

Target Market(s)

Couples, buyers are majority female, between the ages of 20-60

Industry/Entity Type

Tourism

Font styles to use
Sans Serif

Colors

Designer to choose colors to be used in the design.

Requirements
Must have
• Communicate safety, adventure, and romance
• Use images
Nice to have
• There is a lot of text, it would be great if you could make it look like as little text as possible
Should not have
• No childish designs

```html
<!DOCTYPE html>
<html lang="en">
<head>
<meta charset="utf-8">
<title>Skylark Aerial Tours – DL Flyer</title>
<link rel="stylesheet" href="https://fonts.googleapis.com/css2?family=Open+Sans:wght@400;600;700&family=Oswald:wght@300;400&display=swap">
<style>
  :root {
    --gold: #ab8a33;
    --gold-light: #d8c9a3;
    --ink: #2b2b2b;
    --black: #141414;
    --sky-top: #1f6fb8;
    --sky-mid: #8fb9dc;
    --fog: #dfe6ec;
    --field: #5a4a44;
    --page: #ebebeb;
    --white: #ffffff;
  }
  * { box-sizing: border-box; margin: 0; padding: 0; }
  html, body { width: 1200px; height: 1149px; overflow: hidden; background: var(--page); }
  body { position: relative; font-family: "Open Sans", sans-serif; color: var(--ink); }

  .flyer {
    position: absolute; top: 60px; width: 472px; height: 993px;
    background: var(--white); overflow: hidden;
    box-shadow: 0 2px 8px rgba(0,0,0,.25);
  }
  .flyer--front { left: 90px; }
  .flyer--back { left: 628px; }

  .photo { position: absolute; }
  .front-hero {
    left: 0; top: 0; width: 472px; height: 560px;
    background: linear-gradient(180deg, var(--sky-top) 0%, var(--sky-mid) 45%, var(--fog) 62%, #9aa3a8 78%, var(--field) 100%);
  }
  .hero-title {
    position: absolute; top: 18px; left: 0; width: 100%;
    text-align: center; color: var(--white); font-weight: 700;
    font-size: 37px; line-height: 47px; letter-spacing: .2px;
  }
  .wave { position: absolute; left: 0; width: 472px; }

  .photo-circle {
    position: absolute; border-radius: 50%;
    border: 6px solid var(--gold-light);
  }
  .front-circle {
    left: 284px; top: 414px; width: 166px; height: 166px;
    background: radial-gradient(circle at 50% 60%, #ffd35a 0%, #f08a2c 30%, #c24a2a 55%, #2e3f52 80%);
  }

  .tagline {
    position: absolute; top: 593px; left: 0; width: 100%;
    text-align: center; color: var(--gold); font-weight: 600; font-size: 19.5px;
  }
  .tagline-rule { position: absolute; top: 631px; left: 22px; width: 429px; height: 2px; background: var(--gold); }
  .intro {
    position: absolute; top: 651px; left: 10px; width: 452px;
    text-align: center; font-size: 14px; line-height: 17.4px;
  }
  .intro p + p { margin-top: 17px; }

  .book-band {
    position: absolute; left: 0; top: 883px; width: 472px; height: 52px;
    background: var(--gold); color: var(--white);
    display: flex; align-items: center; justify-content: center; gap: 18px;
    font-family: "Oswald", sans-serif; font-weight: 400; font-size: 36px; letter-spacing: .3px;
  }
  .book-band svg { width: 34px; height: 34px; }
  .contact-band {
    position: absolute; left: 0; top: 935px; width: 472px; height: 58px;
    background: linear-gradient(180deg, #2a2a2a, var(--black));
    color: var(--white); text-align: center;
    font-size: 14.5px; line-height: 20px; letter-spacing: 1px; padding-top: 9px;
  }

  .back-hero {
    left: 0; top: 0; width: 472px; height: 300px;
    background: linear-gradient(180deg, #f4f4f2 0%, #b89a6c 30%, #6f7d58 60%, #4f5d64 100%);
  }
  .back-circle {
    left: 286px; top: 170px; width: 168px; height: 168px;
    background: linear-gradient(180deg, #cfe0ee 0%, #f1c14d 35%, #e2493a 55%, #7b8a7a 85%);
  }

  .section-tab {
    position: absolute; left: 0; top: 348px; width: 220px; height: 28px;
    background: var(--gold); color: var(--white);
    border-radius: 0 14px 14px 0; box-shadow: 2px 2px 3px rgba(0,0,0,.2);
    font-weight: 700; font-size: 16px; line-height: 28px; padding-left: 23px;
  }
  .flight-list { position: absolute; top: 398px; left: 22px; width: 440px; list-style: none; font-size: 14px; line-height: 16.5px; }
  .flight-list li { position: relative; padding-left: 19px; margin-bottom: 5px; }
  .flight-list li::before {
    content: ""; position: absolute; left: 0; top: 3px; width: 11px; height: 11px; border-radius: 50%; background: var(--gold);
  }
  .flight-list li::after {
    content: ""; position: absolute; left: 3px; top: 6px; border-left: 5px solid var(--white);
    border-top: 2.5px solid transparent; border-bottom: 2.5px solid transparent;
  }

  .facts {
    position: absolute; left: 20px; top: 562px; width: 436px; height: 134px;
    border: 2px solid var(--gold); border-radius: 10px;
    text-align: center; font-size: 14.5px; line-height: 21.6px; padding-top: 16px;
  }
  .facts h2 {
    position: absolute; top: -14px; left: 50%; transform: translateX(-50%);
    background: var(--white); padding: 0 10px; white-space: nowrap;
    color: var(--gold); font-size: 19.5px; font-weight: 700; line-height: 26px;
  }
  .certificate { position: absolute; left: 21px; top: 708px; width: 215px; font-size: 8.5px; line-height: 11px; font-weight: 600; color: var(--black); }
  .brand-name {
    position: absolute; left: 252px; top: 708px; width: 96px; height: 66px;
    display: flex; flex-direction: column; align-items: center; justify-content: center; gap: 4px;
    font-size: 10.5px; font-weight: 700; color: var(--gold); text-align: center; line-height: 12px;
  }
  .brand-name i { display: block; width: 22px; height: 22px; border-radius: 50%; background: var(--gold); }
  .partner-badge {
    position: absolute; left: 356px; top: 708px; width: 98px; height: 66px;
    border-radius: 50%; background: #2a2320; border: 3px solid var(--gold-light);
  }

  .social { position: absolute; left: 20px; top: 788px; display: flex; gap: 7px; }
  .social span { width: 35px; height: 35px; border-radius: 50%; border: 1.5px solid var(--white); }
  .handle { position: absolute; left: 20px; top: 829px; font-size: 8px; color: #cfcfcf; }
  .more-info {
    position: absolute; left: 0; top: 855px; width: 100%; text-align: center;
    font-family: "Oswald", sans-serif; font-weight: 300; font-size: 18px; color: var(--white); letter-spacing: .3px;
  }
</style>
</head>
<body>

<section class="flyer flyer--front">
  <div class="photo front-hero" role="img" aria-label="Two colourful hot-air balloons floating over a misty valley with mountains at dawn"></div>
  <h1 class="hero-title">KING VALLEY<br>HOT-AIR BALLOONING</h1>
  <svg class="wave" style="top:440px" width="472" height="160" viewBox="0 0 472 160">
    <path d="M0,100 C120,150 270,130 472,40 L472,160 L0,160Z" fill="var(--gold)"/>
    <path d="M0,118 C130,168 290,140 472,62 L472,160 L0,160Z" fill="var(--white)"/>
  </svg>
  <div class="photo photo-circle front-circle" role="img" aria-label="Balloon being inflated with a glowing burner while guests watch at dawn"></div>

  <h2 class="tagline">The perfect gourmet ballooning experience</h2>
  <div class="tagline-rule"></div>
  <div class="intro">
    <p>Live the romance and adventure of flying the beautiful King Valley and surrounds ina hot-air balloon at dawn<br>From the vineyards and patchwork of fields the views expand to the Ovens River, spectacular Mt Buffalo and the High Country beyond<br>The mountain views, once aloft, come to life in dramatic 3D with the early morning light</p>
    <p>Celebrate your flight with a delicious breakfast afterwards (optional)</p>
    <p>Milawa is conveniently located less than an hour's drive from most places in Victoria's North East and Albury in NSW</p>
    <p style="margin-top:14px">Mansfield flights are also available</p>
  </div>

  <div class="book-band">
    <span>BOOK NOW</span>
    <svg viewBox="0 0 34 34" aria-hidden="true"><circle cx="17" cy="17" r="15" fill="none" stroke="#fff" stroke-width="2.5"/><path d="M12,9 l3,0 l1.5,4 l-2,1.5 c1,2.5 2.5,4 5,5 l1.5,-2 l4,1.5 l0,3 c-8,1 -14,-5 -13,-13z" fill="#fff"/></svg>
    <span>1300 555 014</span>
  </div>
  <div class="contact-band">www.skylarkaerialtours.com.au<br>flights@skylarkaerialtours.com.au</div>
</section>

<section class="flyer flyer--back">
  <div class="photo back-hero" role="img" aria-label="Smiling passengers in a balloon basket flying low over a river lined with trees"></div>
  <svg class="wave" style="top:190px" width="472" height="120" viewBox="0 0 472 120">
    <path d="M0,90 C130,120 300,70 472,10 L472,120 L0,120Z" fill="var(--gold)"/>
    <path d="M0,106 C140,134 310,86 472,28 L472,120 L0,120Z" fill="var(--white)"/>
  </svg>
  <div class="photo photo-circle back-circle" role="img" aria-label="Red and yellow balloon rising above farmland"></div>

  <div class="section-tab">YOURFLIGHT</div>
  <ul class="flight-list">
    <li>One-hour sunrise balloon flight in the spectacular King Valley region in North East Victoria</li>
    <li>Delicious champagne breakfast after the flight (recommended option)</li>
    <li>Informative details throughout your experience with our expert crew</li>
    <li>The opportunity to be involved in the inflation and deflation process should you wish</li>
  </ul>

  <div class="facts">
    <h2>KING VALLEY HOT-AIR BALLOONING</h2>
    Safe, friendly and professional<br>
    The flight lasts approximately 1 hour<br>
    The entire experience takes about 3-4 hours<br>
    Suitable from age 7 to 97<br>
    Gift Certificates are also available
  </div>

  <p class="certificate">Skylark Aerial Tours operates under Air Operator's Certificate C100482-15 issued by the National Aviation Safety Regulator</p>
  <div class="brand-name"><i></i>Skylark Aerial Tours</div>
  <div class="partner-badge"></div>

  <svg class="wave" style="top:740px" width="472" height="143" viewBox="0 0 472 143">
    <path d="M0,14 C160,0 260,120 472,42 L472,143 L0,143Z" fill="var(--gold)"/>
    <path d="M0,22 C160,8 260,130 472,52 L472,143 L0,143Z" fill="var(--black)"/>
  </svg>
  <div class="social"><span></span><span></span><span></span></div>
  <p class="handle">@skylarkaerialtours</p>
  <p class="more-info">FOR MORE INFORMATION PLEASE CONTACT US</p>

  <div class="book-band">
    <span>BOOK NOW</span>
    <svg viewBox="0 0 34 34" aria-hidden="true"><circle cx="17" cy="17" r="15" fill="none" stroke="#fff" stroke-width="2.5"/><path d="M12,9 l3,0 l1.5,4 l-2,1.5 c1,2.5 2.5,4 5,5 l1.5,-2 l4,1.5 l0,3 c-8,1 -14,-5 -13,-13z" fill="#fff"/></svg>
    <span>1300 555 014</span>
  </div>
  <div class="contact-band">www.skylarkaerialtours.com.au<br>flights@skylarkaerialtours.com.au</div>
</section>

</body>
</html>
```